" Os clientes entram em nosso site e preenchem os dados para solicitar uma cotação de seguro ou nos contatam com interesse de fazer algum seguro. Após este contato inicial, entramos em contato para solicitar informações complementares e realizamos as cotações nas seguradoras ou empresas de medicina em grupo. Um terceiro passo é entrar em contato com o cliente e enviar as opções de valores para ele fazer a escolha do que melhor atende ele. Então efetivamos o seguro e damos suporte pós venda caso aconteça algum incidente coberto pelo seguro. Principais produtos: - Seguro de Saúde - Seguro de Automóvel - Seguro de Viagem - Seguro de Vida - Seguro Residencial - Seguro Fiança Locatícia - Seguro de Saúde (Empresas) - Seguro de Vida (Empresas) - Seguro Empresarial (Empresas) - Seguro de Transporte (Empresas) - Seguro de Riscos de Engenharia (Empresas) - Seguro Responsabilidade Civil (Empresas) "

```html
<!DOCTYPE html>
<html lang="pt-BR">
<head>
<meta charset="UTF-8">
<title>Seguro Saúde – Velmora Plus</title>
<link rel="stylesheet" href="https://fonts.googleapis.com/css2?family=Montserrat:wght@300;400;500;600&display=swap">
<style>
  :root{
    --teal:#3aa5a3;
    --teal-deep:#2c7f8c;
    --ink-grey:#5a5f63;
    --orange:#e8792b;
    --white:#ffffff;
    --wall:#e6c9b4;
    --wall-deep:#c99f86;
    --coat:#f4efe9;
    --sweater:#b9b6ae;
    --hair:#dcdad5;
    --window:#efe6dc;
  }
  html,body{margin:0;padding:0;overflow:hidden;background:#fff;}
  .poster{position:relative;width:1200px;height:1200px;overflow:hidden;background:var(--white);font-family:"Montserrat",sans-serif;}
  .hero-photo{position:absolute;left:0;top:0;width:1200px;height:940px;
    background:
      radial-gradient(ellipse 260px 340px at 230px 760px, rgba(246,242,237,0.95), rgba(246,242,237,0) 100%),
      radial-gradient(ellipse 120px 150px at 250px 400px, rgba(176,124,96,0.55), rgba(176,124,96,0) 100%),
      radial-gradient(ellipse 260px 380px at 690px 720px, rgba(185,182,174,0.95), rgba(185,182,174,0) 100%),
      radial-gradient(ellipse 150px 180px at 590px 260px, rgba(220,218,213,0.95), rgba(220,218,213,0) 100%),
      radial-gradient(ellipse 200px 520px at 1130px 520px, rgba(239,230,220,0.9), rgba(239,230,220,0) 100%),
      linear-gradient(100deg,#dcc5b6 0%,var(--wall) 40%,var(--wall-deep) 75%,var(--window) 100%);}
  .hero-tint{position:absolute;inset:0;background:linear-gradient(180deg,rgba(255,255,255,0.1),rgba(58,165,163,0.06));}
  .footer-curve{position:absolute;left:0;top:0;width:1200px;height:1200px;}
  .headline{position:absolute;right:28px;top:44px;margin:0;text-align:right;color:var(--teal);
    font-weight:500;font-size:112px;line-height:116px;letter-spacing:-3px;}
  .tagline{position:absolute;right:28px;top:285px;margin:0;text-align:right;color:var(--white);
    font-weight:300;font-size:42px;line-height:52px;letter-spacing:0.5px;}
  .brand{position:absolute;left:20px;top:935px;width:380px;text-align:center;}
  .brand-mark{display:block;width:104px;height:104px;margin:0 auto 30px;border-radius:50%;background:var(--teal-deep);}
  .brand-name{display:block;white-space:nowrap;color:var(--teal-deep);font-weight:600;font-size:38px;line-height:44px;}
  .brand-sub{display:block;white-space:nowrap;color:var(--ink-grey);font-weight:400;font-size:26px;line-height:36px;}
  .contacts{position:absolute;right:28px;top:968px;margin:0;padding:0;list-style:none;text-align:right;}
  .contacts li{display:flex;justify-content:flex-end;align-items:center;gap:22px;color:var(--teal-deep);
    font-size:28px;font-weight:400;height:44px;white-space:nowrap;}
  .contacts li.gap{margin-top:18px;}
  .contacts svg{width:28px;height:28px;flex:none;}
  .icon-spacer{width:28px;height:28px;flex:none;}
</style>
</head>
<body>
<div class="poster">
  <div class="hero-photo" role="img" aria-label="Foto de um médico sorridente de jaleco branco e estetoscópio conversando com uma paciente idosa de cabelos grisalhos">
    <div class="hero-tint"></div>
  </div>

  <svg class="footer-curve" viewBox="0 0 1200 1200" aria-hidden="true">
    <path d="M0 770 Q600 1010 1200 870 L1200 1200 L0 1200 Z" fill="#ffffff"/>
    <path d="M0 790 Q600 1010 1200 880" fill="none" stroke="var(--teal)" stroke-width="7"/>
  </svg>

  <h1 class="headline">SEGURO<br>SAÚDE</h1>
  <p class="tagline">CUIDE DO SEU BEM<br>MAIS PRECIOSO</p>

  <div class="brand">
    <span class="brand-mark"></span>
    <span class="brand-name">VELMORA PLUS</span>
    <span class="brand-sub">Corretora de Seguros</span>
  </div>

  <ul class="contacts">
    <li>(00) 97412-3658
      <svg viewBox="0 0 24 24"><path fill="var(--orange)" d="M6.6 10.8a15 15 0 0 0 6.6 6.6l2.2-2.2c.3-.3.7-.4 1-.2 1.1.4 2.3.6 3.6.6.6 0 1 .4 1 1V20c0 .6-.4 1-1 1A17 17 0 0 1 3 4c0-.6.4-1 1-1h3.5c.6 0 1 .4 1 1 0 1.3.2 2.5.6 3.6.1.3 0 .7-.2 1z"/></svg>
    </li>
    <li>(00) 3526-4190<span class="icon-spacer"></span></li>
    <li class="gap">contato@velmora.com.br
      <svg viewBox="0 0 24 24"><rect x="2" y="5" width="20" height="14" rx="1.5" fill="var(--orange)"/><path d="M3 6l9 7 9-7" fill="none" stroke="#fff" stroke-width="1.6"/></svg>
    </li>
    <li class="gap">www.velmoraplus.com.br
      <svg viewBox="0 0 24 24"><circle cx="12" cy="12" r="10" fill="var(--orange)"/><path d="M2 12h20M12 2c3 3 3 17 0 20M12 2c-3 3-3 17 0 20" fill="none" stroke="#fff" stroke-width="1.3"/></svg>
    </li>
  </ul>
</div>
</body>
</html>
```